Card design for orthopaedic surgeons working as The Meridale Orthopaedic Clinic

Business cards, letterhead

Colors

Designer to choose colors to be used in the design.

Requirements
Must have
• Late addition.
• Cards letterhead must have logos of
• Corvane Federated Guild of Surgeons
• Tellmark Orthopaedic Society
Nice to have
• Back of card to have space for appointment time to be added by hand and some blank space for writing incidental other notes.

```html
<!DOCTYPE html>
<html lang="en">
<head>
<meta charset="utf-8">
<title>The Meridale Orthopaedic Clinic – Business Card</title>
<link rel="stylesheet" href="https://fonts.googleapis.com/css2?family=Ubuntu:wght@400;500&display=swap">
<style>
  :root {
    --navy: #05324c;
    --sky: #33b0fc;
    --white: #ffffff;
    --contact: #eaf3f9;
    --backdrop: #e9ecef;
  }
  * { box-sizing: border-box; margin: 0; padding: 0; }
  html, body {
    width: 1125px;
    height: 1200px;
    overflow: hidden;
    background: var(--backdrop);
    font-family: "Ubuntu", "Trebuchet MS", sans-serif;
  }
  .card {
    position: absolute;
    left: 162px;
    width: 800px;
    height: 455px;
    border-radius: 24px;
    overflow: hidden;
  }
  .card-front { top: 105px; background: var(--white); }
  .card-back { top: 622px; background: var(--sky); }

  .front-waves { position: absolute; inset: 0; width: 800px; height: 455px; }

  .identity { position: absolute; left: 68px; top: 48px; }
  .identity .name {
    color: var(--sky);
    font-size: 33px;
    font-weight: 500;
    letter-spacing: 0.8px;
    line-height: 1;
  }
  .identity .role {
    color: var(--contact);
    font-size: 18px;
    font-weight: 400;
    letter-spacing: 1.2px;
    margin-top: 6px;
  }

  .contact {
    position: absolute;
    right: 66px;
    top: 50px;
    list-style: none;
    color: var(--contact);
    font-size: 16.5px;
    font-weight: 400;
    text-align: right;
  }
  .contact li {
    display: flex;
    justify-content: flex-end;
    align-items: center;
    gap: 12px;
    height: 22.5px;
  }
  .contact li.gap { margin-top: 11px; }
  .contact .icon { width: 15px; height: 15px; flex: none; fill: var(--sky); }

  .clinic-name {
    position: absolute;
    left: 66px;
    top: 362px;
    color: var(--navy);
    font-size: 28px;
    font-weight: 400;
    letter-spacing: -0.2px;
  }

  .back-url {
    position: absolute;
    left: 0;
    right: 0;
    top: 380px;
    text-align: center;
    color: var(--white);
    font-size: 17px;
    font-weight: 400;
    letter-spacing: 11px;
    text-indent: 11px;
  }
</style>
</head>
<body>

<section class="card card-front">
  <svg class="front-waves" viewBox="0 0 800 455" aria-hidden="true">
    <path fill="var(--navy)" d="M0,310 C90,240 165,200 250,200 C380,200 470,280 600,298 C690,308 750,285 800,252 V0 H0 Z"/>
    <path fill="var(--sky)" d="M0,318 C95,252 175,212 255,212 C385,212 470,288 605,305 C695,314 755,292 800,265 L800,272 C750,308 690,330 610,325 C470,316 390,225 255,222 C180,222 100,262 5,320 Z"/>
  </svg>

  <div class="identity">
    <h1 class="name">DANIEL WHITCOMBE</h1>
    <p class="role">PRESIDENT</p>
  </div>

  <ul class="contact">
    <li>214 Harrowgate Road
      <svg class="icon" viewBox="0 0 16 16"><path d="M8 0a5.5 5.5 0 0 0-5.5 5.5C2.5 10 8 16 8 16s5.5-6 5.5-10.5A5.5 5.5 0 0 0 8 0zm0 8a2.5 2.5 0 1 1 0-5 2.5 2.5 0 0 1 0 5z"/></svg>
    </li>
    <li>Fenwick Bay, Larsen 40912 <span class="icon"></span></li>
    <li class="gap">555-204-7731
      <svg class="icon" viewBox="0 0 16 16"><path d="M3.6 0.5l2.2 3.3-1.4 1.6c.9 2.2 2.6 3.9 4.8 4.8l1.6-1.4 3.3 2.2-.9 2.9C8 13.6 2.4 8 2.3 1.4z"/></svg>
    </li>
    <li>555-318-9024
      <svg class="icon" viewBox="0 0 16 16"><path d="M4 0h8a1 1 0 0 1 1 1v14a1 1 0 0 1-1 1H4a1 1 0 0 1-1-1V1a1 1 0 0 1 1-1zm1 2v10h6V2zm3 11a1 1 0 1 0 0 2 1 1 0 0 0 0-2z"/></svg>
    </li>
    <li>555-427-6150
      <svg class="icon" viewBox="0 0 16 16"><path d="M4 2h8v4H4zM1 7h14v6h-3v-2H4v2H1zm3 5h8v3H4z"/></svg>
    </li>
    <li>daniel@meridaleclinic.com
      <svg class="icon" viewBox="0 0 16 16"><path d="M1 3h14v1.2L8 8.6 1 4.2zm0 2.6l7 4.4 7-4.4V13H1z"/></svg>
    </li>
    <li>www.meridaleclinic.com
      <svg class="icon" viewBox="0 0 16 16"><path d="M8 0a8 8 0 1 0 0 16A8 8 0 0 0 8 0zm-1 2.5c1 .8 1.2 2 .4 2.8-.9.8-2.4.4-2.6 1.8-.2 1.1 1.3 1.4 1.8 2.4.4 1-.2 2.4-.6 3.3A6 6 0 0 1 7 2.5zm3 1.2c1.5.5 3 2 3.3 3.8-1 .3-2-.5-2.9-.2-.9.4-.7 2-1.6 2.2-.8.1-1.3-1-1-1.9.4-1 1.8-1.3 2-2.4.1-.5-.1-1-.2-1.5z"/></svg>
    </li>
  </ul>

  <p class="clinic-name">The Meridale Orthopaedic Clinic</p>
</section>

<section class="card card-back">
  <p class="back-url">WWW.MERIDALECLINIC.COM</p>
</section>

</body>
</html>
```